Online-Gutschein-Design für Mobilfunkhändler
Zielgruppe
https://shop.velantra-beispiel.at/
Velantra ist ein erfahrener Mobilfunkhändler und blickt auf jahrelange Erfahrung beim Vertrieb von Smartphones und Mobilfunk Zubehör zurück.
Aufgabenstellung
Farbcode: #A46CA0
VELANTRA Logo
Kluge Geräte mit Schwung
Online Gutschein für Dich im Wert von ... € 5,-
Nur in unserem Onlineshop auf shop.velantra-beispiel.at einlösbar.
Gutschein nur einmalig und auf shop.velantra-beispiel.at bis 31.12.2021 gültig.
Ausgenommen Sonderangebote. Keine Barablöse.
INFO:
Bilder und Logo können bei Bedarf vorab über unseren Online Shop heruntergeladen werden. Bei Finalisierung werden die Dateien bereitgestellt.
Passender Formulierungen und Ideen gefragt.
Wir vergeben den Gutschein an Kunden, die bei uns im POS (Shop vor Ort) kein Zubehör oder ähnliches für ihr Handy kaufen und möchte sie dadurch animieren, in unserem Online Shop später zu Hause etwas zu kaufen.
Format: A5 und beidseitig bitte. Vorder + Rückseite. Ideen sind auch hier gewünscht daher keine strikte Vorgabe.
Der Gutschein soll unsere Kunden animieren, unseren Online Shop zu besuchen und im besten Fall den Gutschein einzulösen...
Folge Aufträge sind angedacht!

```html
<!DOCTYPE html>
<html lang="de">
<head>
<meta charset="utf-8">
<title>Velantra Online Gutschein</title>
<link rel="stylesheet" href="https://fonts.googleapis.com/css2?family=Barlow:ital,wght@0,400;0,600;0,700;1,600&family=Barlow+Semi+Condensed:wght@700&display=swap">
<style>
  :root {
    --brand: #a46ca0;
    --ink: #111111;
    --paper: #ffffff;
    --stage: #f1eef1;
    --phone-dark: #1c1c1e;
    --phone-warm: #c89a72;
  }
  html, body {
    margin: 0;
    width: 1200px;
    height: 1200px;
    overflow: hidden;
    background: var(--stage);
  }
  .voucher {
    position: absolute;
    left: 40px;
    top: 206px;
    width: 1120px;
    height: 787px;
    background: var(--paper);
    overflow: hidden;
    font-family: "Barlow", Arial, sans-serif;
  }
  .brand-name {
    position: absolute;
    left: 45px;
    top: 36px;
    margin: 0;
    font-family: "Barlow Semi Condensed", "Arial Narrow", sans-serif;
    font-weight: 700;
    font-size: 64px;
    line-height: 1;
    letter-spacing: 2px;
    color: var(--ink);
  }
  .tagline {
    position: absolute;
    left: 45px;
    top: 108px;
    margin: 0;
    font-style: italic;
    font-weight: 600;
    font-size: 23px;
    color: var(--brand);
  }
  .shop-url {
    position: absolute;
    right: 70px;
    top: 56px;
    margin: 0;
    font-weight: 700;
    font-size: 27px;
    color: var(--brand);
  }
  .product-visual {
    position: absolute;
    left: 160px;
    top: 172px;
    width: 300px;
    height: 520px;
    border-radius: 46px;
    background: linear-gradient(170deg, #3a3a3c 0%, var(--phone-dark) 35%, #4a3b30 70%, var(--phone-warm) 100%);
    box-shadow: 0 18px 30px rgba(0,0,0,.18);
  }
  .headline {
    position: absolute;
    right: 72px;
    top: 166px;
    margin: 0;
    text-align: right;
    font-family: "Barlow Semi Condensed", "Arial Narrow", sans-serif;
    font-weight: 700;
    font-size: 106px;
    line-height: 97px;
    color: var(--brand);
  }
  .headline .for-you {
    display: block;
    font-size: 100px;
  }
  .headline .for { color: var(--ink); }
  .value-badge {
    position: absolute;
    left: 748px;
    top: 470px;
    width: 320px;
    height: 172px;
  }
  .value-badge text {
    font-family: "Barlow Semi Condensed", "Arial Narrow", sans-serif;
    font-weight: 700;
    fill: var(--paper);
  }
  .footnote {
    position: absolute;
    right: 50px;
    top: 684px;
    margin: 0;
    font-size: 12px;
    white-space: nowrap;
    color: var(--brand);
  }
  .footnote strong { font-weight: 700; }
  .footer-wave {
    position: absolute;
    left: 0;
    top: 0;
    width: 1120px;
    height: 787px;
  }
  .terms {
    position: absolute;
    left: 78px;
    top: 745px;
    margin: 0;
    font-size: 12.5px;
    line-height: 18px;
    color: var(--paper);
  }
</style>
</head>
<body>
  <main class="voucher">
    <svg class="footer-wave" viewBox="0 0 1120 787" aria-hidden="true">
      <path d="M0,722 C350,745 750,745 1120,712 L1120,787 L0,787 Z" fill="#a46ca0"/>
    </svg>

    <h1 class="brand-name">VELANTRA</h1>
    <p class="tagline">Kluge Geräte mit Schwung</p>
    <p class="shop-url">shop.velantra-beispiel.at</p>

    <div class="product-visual" role="img" aria-label="Smartphone, aus dessen Bildschirm eine Hand schwarze Geschenkboxen mit goldener Schleife und Konfetti reicht"></div>

    <h2 class="headline">Online<br>Gutschein<span class="for-you"><span class="for">für</span> Dich</span></h2>

    <svg class="value-badge" viewBox="0 0 320 172" role="img" aria-label="Gutscheinwert 5 Euro">
      <ellipse cx="160" cy="86" rx="159" ry="85" fill="#a46ca0"/>
      <text x="150" y="126" text-anchor="middle" font-size="118">€5,–</text>
      <text x="262" y="52" text-anchor="middle" font-size="44">*</text>
    </svg>

    <p class="footnote">*Nur in unserem Onlineshop auf <strong>shop.velantra-beispiel.at</strong> einlösbar.</p>

    <p class="terms">Gutschein nur einmalig und auf shop.velantra-beispiel.at bis <strong>31.12.2021</strong> gültig.<br>Ausgenommen Sonderangebote. Keine Barablöse.</p>
  </main>
</body>
</html>
```